Bramwell Tideworks Pools: Transforming Backyards into Luxury Retreats!

We’d love your help in making our Facebook page look more professional.
Bramwell Tideworks Pools
Bramwell Tideworks Pools is a premier construction company dedicated to transforming your outdoor dreams into reality with expert craftsmanship and innovative design.
22 years serving our community (Montgomery, Texas) and surrounding areas
bramwelltidetx@mailorbit,com
281-756-2149
Free Consultation
Color Palette:
Shades of blue (navy, aqua, teal) to represent water, trust, and tranquility.
White and light gray for a clean, modern look.
Earth tones (sand, beige, stone textures) to connect with natural outdoor environments.
Sleek, modern but elegant fonts for a luxury appeal
Target Market(s)
1. Homeowners Seeking Luxury & Customization High-income families or individuals who want a custom-designed pool. People looking to upgrade their backyard into a luxury outdoor space. Homeowners who value quality craftsmanship over budget options. 2. New Homeowners & Property Developers People moving into new homes who want to add a high-end pool. Custom home builders and property developers looking for pool contractors. 3. Families & Entertainers Families who want a safe and stylish pool for kids. Homeowners who frequently entertain guests and need a pool as a centerpiece. 4. High-End & Resort-Style Property Owners Vacation home and Staylodge owners investing in outdoor appeal. Resorts, luxury rentals, or boutique hotels that need custom pools. 5. Renovation & Remodeling Clients Homeowners with older pools looking for modern upgrades. People wanting energy-efficient pool designs or smart automation features.
Industry/Entity Type
Construction

```html
<!DOCTYPE html>
<html lang="en">
<head>
<meta charset="utf-8">
<title>Bramwell Tideworks Pools – Cover</title>
<link href="https://fonts.googleapis.com/css2?family=Jost:ital,wght@0,400;0,500;1,500;1,800;1,900&display=swap" rel="stylesheet">
<style>
  :root{
    --navy:#0b2a6b;
    --royal:#0a4fb8;
    --ocean:#0a6fc0;
    --sky:#1e9bf0;
    --white:#ffffff;
    --ink:#141414;
  }
  *{margin:0;padding:0;box-sizing:border-box}
  html,body{width:1200px;height:1200px;overflow:hidden}
  body{background:var(--navy);font-family:"Jost",sans-serif;position:relative}
  .cover{position:absolute;left:40px;top:394px;width:1120px;height:412px;background:var(--white);overflow:hidden}
  .cover svg{position:absolute;left:0;top:0}
  .headline{position:absolute;left:61px;top:20px;color:var(--royal);line-height:.92;letter-spacing:-1px;white-space:nowrap}
  .headline .strong{font-weight:900;font-style:italic}
  .headline .light{font-weight:400}
  .headline .line1{font-size:56px;display:block}
  .headline .line2{font-size:53px;display:block}
  .tagline{position:absolute;left:61px;top:128px;font-size:30px;font-weight:500;color:var(--ink);line-height:1.08;letter-spacing:-.2px;white-space:nowrap}
  .service-band{position:absolute;left:63px;top:209px;width:524px;height:64px;background:var(--ocean);border-radius:6px;color:var(--white);font-weight:800;font-style:italic;font-size:16px;line-height:1.3;padding:11px 16px;text-transform:uppercase;white-space:nowrap;letter-spacing:-.2px}
  .offer{position:absolute;left:64px;top:290px;color:var(--royal);font-weight:900;font-style:italic;font-size:23px;line-height:1.08;text-transform:uppercase}
  .contact{position:absolute;left:270px;top:278px;white-space:nowrap}
  .contact .prompt{font-size:19px;font-style:italic;font-weight:500;color:var(--ink);text-transform:uppercase;line-height:1.1}
  .contact .phone{font-size:38px;font-weight:900;font-style:italic;color:var(--royal);line-height:1;margin-top:4px;letter-spacing:.5px}
  .contact .email{font-size:17px;font-weight:800;font-style:italic;color:var(--royal);line-height:1.1}
  .thumb{position:absolute;width:232px;height:95px;border:4px solid var(--white);border-radius:6px;box-shadow:0 3px 8px rgba(0,0,0,.35);transform:skewX(-2deg)}
  .thumb.one{left:630px;top:178px;background:linear-gradient(180deg,#6aa3e0 0%,#a9c9ea 30%,#4d6a44 55%,#cfd3d2 72%,#53c0d6 82%,#d8d8d2 100%)}
  .thumb.two{left:630px;top:288px;background:linear-gradient(180deg,#7fb2e6 0%,#b8d4ee 28%,#3d6c3a 45%,#5e8f3c 60%,#5cc3d6 78%,#d9d9d4 100%)}
</style>
</head>
<body>
  <section class="cover">
    <svg width="1120" height="412" viewBox="0 0 1120 412" aria-hidden="true">
      <defs>
        <linearGradient id="waveFill" x1="0" y1="0" x2="1" y2="0">
          <stop offset="0" stop-color="#1aa3f5"/>
          <stop offset="1" stop-color="#0a4fb8"/>
        </linearGradient>
      </defs>
      <path class="bottom-wave" d="M0,284 C30,350 90,380 220,384 C420,390 560,366 780,366 L780,412 L0,412 Z" fill="url(#waveFill)"/>
      <path class="frame-curve" d="M730,0 C660,20 610,50 608,100 C606,160 640,220 650,270 L700,412 L800,412 Z" fill="var(--royal)"/>
    </svg>
    <svg width="1120" height="412" viewBox="0 0 1120 412" role="img" aria-label="Photo of a luxury home with a rectangular pool and stone deck under a sunny sky">
      <defs>
        <linearGradient id="photoFill" x1="0" y1="0" x2="0" y2="1">
          <stop offset="0" stop-color="#3f86d6"/>
          <stop offset=".22" stop-color="#8fb8de"/>
          <stop offset=".42" stop-color="#4f5a55"/>
          <stop offset=".58" stop-color="#4d7a47"/>
          <stop offset=".7" stop-color="#3bb1c8"/>
          <stop offset=".84" stop-color="#8d8c86"/>
          <stop offset="1" stop-color="#a09f98"/>
        </linearGradient>
      </defs>
      <path d="M748,0 C680,25 640,60 640,110 C640,170 670,230 690,290 L755,412 L1120,412 L1120,0 Z" fill="url(#photoFill)"/>
    </svg>

    <h1 class="headline">
      <span class="line1"><span class="strong">TRANSFORM</span> <span class="light">YOUR</span></span>
      <span class="line2 strong">OUTDOOR DREAMS</span>
    </h1>
    <p class="tagline">Into Rreality With Expert Craftsmanship<br>and Innovative Design</p>
    <p class="service-band">22 Years Serving Our Community (Montgomery,<br>Texas) and Surrounding Areas</p>
    <p class="offer">Free<br>Consultation</p>
    <div class="contact">
      <p class="prompt">Contact us today!</p>
      <p class="phone">281-756-2149</p>
      <p class="email">bramwelltidetx@mailorbit,com</p>
    </div>
    <div class="thumb one" role="img" aria-label="Photo of a lakeside home with a pool and trees"></div>
    <div class="thumb two" role="img" aria-label="Photo of a pool and spa overlooking a lake"></div>
  </section>
</body>
</html>
```